Maple Ridge business card design

Card needs to include the following text/items:
Company Logo
Tobin Marsh
Phone # - 555-318-7642
service@mapleridgelandscaping.example
Lawn & landscape maintenance services

```html
<!DOCTYPE html>
<html lang="en">
<head>
<meta charset="utf-8">
<title>Maple Ridge Landscaping – Business Card</title>
<link rel="stylesheet" href="https://fonts.googleapis.com/css2?family=Gelasio:wght@400;700&display=swap">
<style>
  :root {
    --backdrop: #013a47;
    --forest: #015e2d;
    --olive: #718f05;
    --paper: #ffffff;
    --ink-dark: #0d4a26;
    --shadow: rgba(0, 10, 15, 0.55);
  }
  * { margin: 0; padding: 0; box-sizing: border-box; }
  html, body { width: 927px; height: 1200px; overflow: hidden; }
  body {
    background: var(--backdrop);
    font-family: "Gelasio", Georgia, serif;
    position: relative;
  }
  .card {
    position: absolute;
    left: 113px;
    width: 701px;
    height: 400px;
    box-shadow: 18px 22px 26px var(--shadow);
    overflow: hidden;
  }
  .card--front { top: 145px; background: var(--forest); }
  .card--back { top: 654px; background: var(--paper); }
  .card__shape { position: absolute; inset: 0; width: 701px; height: 400px; }
  .brand {
    position: absolute;
    left: 0; right: 0; top: 52px;
    display: flex; flex-direction: column; align-items: center;
  }
  .brand__circle {
    width: 150px; height: 150px; border-radius: 50%;
    background: var(--forest);
  }
  .brand__name {
    margin-top: 14px;
    font-size: 38px; font-weight: 700;
    color: var(--ink-dark);
    letter-spacing: 0.5px;
    line-height: 1;
  }
  .tagline {
    position: absolute; left: 0; right: 0; top: 333px;
    text-align: center; color: var(--paper);
    font-size: 22px; line-height: 1.2;
  }
  .contact { position: absolute; left: 0; right: 0; text-align: center; color: var(--paper); }
  .contact--name { top: 146px; font-size: 28px; font-weight: 700; letter-spacing: 3.5px; }
  .contact--phone { top: 199px; font-size: 19px; }
  .contact--email { top: 339px; font-size: 19px; }
</style>
</head>
<body>
  <section class="card card--front">
    <svg class="card__shape" viewBox="0 0 701 400" aria-hidden="true">
      <path id="notch" d="M 22 -5 C 40 10, 48 30, 46 60 C 44 100, 44 120, 62 130 C 85 145, 118 150, 124 175 C 128 200, 125 215, 160 228 C 195 240, 215 240, 225 270 C 232 290, 240 296, 260 296 L 440 296 C 460 296, 468 290, 475 270 C 485 240, 505 240, 540 228 C 575 215, 572 200, 576 175 C 582 150, 615 145, 638 130 C 656 120, 656 100, 654 60 C 652 30, 660 10, 678 -5 Z" fill="var(--paper)" stroke="var(--olive)" stroke-width="20"/>
      <path d="M 22 -5 C 40 10, 48 30, 46 60 C 44 100, 44 120, 62 130 C 85 145, 118 150, 124 175 C 128 200, 125 215, 160 228 C 195 240, 215 240, 225 270 C 232 290, 240 296, 260 296 L 440 296 C 460 296, 468 290, 475 270 C 485 240, 505 240, 540 228 C 575 215, 572 200, 576 175 C 582 150, 615 145, 638 130 C 656 120, 656 100, 654 60 C 652 30, 660 10, 678 -5 Z" fill="var(--paper)"/>
    </svg>
    <div class="brand">
      <div class="brand__circle"></div>
      <div class="brand__name">Maple Ridge</div>
    </div>
    <p class="tagline">Lawn &amp; landscape maintenance services</p>
  </section>

  <section class="card card--back">
    <svg class="card__shape" viewBox="0 0 701 400" aria-hidden="true">
      <g transform="translate(0 400) scale(1 -1)">
        <path d="M 22 -5 C 40 10, 48 30, 46 60 C 44 100, 44 120, 62 130 C 85 145, 118 150, 124 175 C 128 200, 125 215, 160 228 C 195 240, 215 240, 225 270 C 232 290, 240 296, 260 296 L 440 296 C 460 296, 468 290, 475 270 C 485 240, 505 240, 540 228 C 575 215, 572 200, 576 175 C 582 150, 615 145, 638 130 C 656 120, 656 100, 654 60 C 652 30, 660 10, 678 -5 Z" fill="var(--forest)" stroke="var(--olive)" stroke-width="20"/>
        <path d="M 22 -5 C 40 10, 48 30, 46 60 C 44 100, 44 120, 62 130 C 85 145, 118 150, 124 175 C 128 200, 125 215, 160 228 C 195 240, 215 240, 225 270 C 232 290, 240 296, 260 296 L 440 296 C 460 296, 468 290, 475 270 C 485 240, 505 240, 540 228 C 575 215, 572 200, 576 175 C 582 150, 615 145, 638 130 C 656 120, 656 100, 654 60 C 652 30, 660 10, 678 -5 Z" fill="var(--forest)"/>
      </g>
    </svg>
    <p class="contact contact--name">Tobin Marsh</p>
    <p class="contact contact--phone">Phone # - 555-318-7642</p>
    <p class="contact contact--email">service@mapleridgelandscaping.example</p>
  </section>
</body>
</html>
```